indoor tennis and sports center( club)

we need a logo for a new business venture, it will be for business cards and for presentations.
presentations for potential investors and authorities.
the design needs to communicate the sport and a community of tennis players
the center includes a tennis academy, and sports club with training sessions for all ages

Project Deadline Extended
Reason: so that I can get some more feedback on my side as to te design we want

Target Market(s)

potential investors or partners

Industry/Entity Type

Business

Contact Information for Business Card

i need the name of the club
names of the partners
slogan" changing lives through tennis" on the front
the clubs three main goals are ports education , academy and a community club

Colors
3176b5
33b8a4
fbee3d
0dac94
acd036

Requirements
Must have
• a strong logo
• names of the partners
• web site and email address
• tel number
Nice to have
• a connection between the different aspects of the club

```html
<!DOCTYPE html>
<html lang="en">
<head>
<meta charset="utf-8">
<title>Baseline Hall – Business Cards</title>
<link rel="stylesheet" href="https://fonts.googleapis.com/css2?family=Michroma&family=Open+Sans:wght@400;600;700&display=swap">
<style>
  :root {
    --lime: #8dcb1c;
    --lime-deep: #5ea51a;
    --lime-mid: #76bb1b;
    --violet: #1f0a48;
    --violet-soft: #2a1158;
    --lilac: #b36ee0;
    --white: #ffffff;
    --page: #ecebe7;
  }
  * { margin: 0; padding: 0; box-sizing: border-box; }
  html, body { width: 1200px; height: 900px; overflow: hidden; }
  body {
    background: var(--page);
    font-family: "Open Sans", Arial, sans-serif;
    position: relative;
  }
  .card {
    position: absolute;
    top: 295px;
    width: 540px;
    height: 310px;
    overflow: hidden;
    box-shadow: 0 6px 18px rgba(0,0,0,0.18);
  }
  .card--front { left: 40px; background: linear-gradient(135deg, var(--lime) 0%, var(--lime-mid) 55%, var(--lime-deep) 100%); }
  .card--back { left: 620px; background: var(--violet); }

  .wordmark {
    font-family: "Michroma", Arial, sans-serif;
    letter-spacing: 1px;
    display: flex;
    align-items: center;
    gap: 10px;
    white-space: nowrap;
  }
  .wordmark__dot { border-radius: 50%; flex: none; }
  .club-line {
    font-family: "Open Sans", Arial, sans-serif;
    font-weight: 600;
    text-transform: uppercase;
    white-space: nowrap;
  }

  /* front */
  .front__brand { position: absolute; left: 60px; top: 52px; }
  .front__brand .wordmark { color: var(--white); font-size: 34px; }
  .front__brand .wordmark__dot { width: 22px; height: 22px; background: var(--white); }
  .front__brand .club-line { color: var(--white); font-size: 16px; margin-top: 2px; letter-spacing: 0.3px; }
  .pillars {
    position: absolute; left: 0; right: 0; top: 130px; height: 72px;
    background: var(--violet);
    display: flex; align-items: center; justify-content: center; gap: 44px;
  }
  .pillar { color: var(--white); font-size: 19px; display: flex; align-items: center; gap: 8px; }
  .pillar::before {
    content: ""; width: 14px; height: 14px; border-radius: 50%;
    background: radial-gradient(circle at 35% 35%, #b6ea3c, var(--lime-deep));
  }
  .front__slogan {
    position: absolute; left: 0; right: 0; top: 222px; text-align: center;
    font-family: "Michroma", Arial, sans-serif; font-size: 18px; letter-spacing: 2px;
    color: var(--violet); text-transform: uppercase;
  }

  /* back */
  .back__band {
    position: absolute; left: 0; right: 0; top: 172px; height: 76px;
    background: linear-gradient(90deg, var(--lime-deep), var(--lime) 50%, var(--lime-deep));
  }
  .back__brand { position: absolute; left: 205px; top: 62px; }
  .back__brand .wordmark { color: var(--lime); font-size: 23px; }
  .back__brand .wordmark__dot { width: 15px; height: 15px; background: var(--lime); }
  .back__brand .club-line { color: var(--white); font-size: 11px; }
  .website { color: var(--lilac); font-size: 13px; margin-top: 10px; }
  .person { position: absolute; right: 300px; top: 172px; text-align: right; }
  .person__name { color: var(--white); font-weight: 700; font-size: 18px; text-transform: uppercase; line-height: 1.2; margin-top: 14px; }
  .person__role { color: var(--white); font-size: 13px; }
  .divider { position: absolute; left: 254px; top: 152px; width: 1px; height: 74px; background: rgba(255,255,255,0.5); }
  .contacts { position: absolute; left: 266px; top: 146px; color: var(--white); font-size: 12px; line-height: 1.9; }
  .contacts li { list-style: none; display: flex; align-items: center; gap: 6px; }
  .contacts svg { width: 12px; height: 12px; fill: var(--white); }
  .back__slogan {
    position: absolute; left: 0; right: 0; top: 268px; text-align: center;
    font-family: "Michroma", Arial, sans-serif; font-size: 17px; letter-spacing: 1.5px;
    color: var(--lime); text-transform: uppercase;
  }
</style>
</head>
<body>
  <section class="card card--front" aria-label="Card front">
    <div class="front__brand">
      <div class="wordmark"><span>BASELINE HALL</span><span class="wordmark__dot"></span></div>
      <div class="club-line">Israel indoor racquets and fitness club</div>
    </div>
    <div class="pillars">
      <span class="pillar">Indoor Club</span>
      <span class="pillar">Academy</span>
      <span class="pillar">Education</span>
    </div>
    <p class="front__slogan">Building a community</p>
  </section>

  <section class="card card--back" aria-label="Card back">
    <div class="back__band"></div>
    <div class="back__brand">
      <div class="wordmark"><span>BASELINE HALL</span><span class="wordmark__dot"></span></div>
      <div class="club-line">Israel indoor racquets and fitness club</div>
      <p class="website">www.baselinehall.net</p>
    </div>
    <div class="person">
      <p class="person__name">Dana Levran</p>
      <p class="person__role">Founder</p>
    </div>
    <div class="divider"></div>
    <ul class="contacts">
      <li><svg viewBox="0 0 24 24" aria-hidden="true"><path d="M6.6 10.8a15.1 15.1 0 0 0 6.6 6.6l2.2-2.2a1 1 0 0 1 1-.25 11.4 11.4 0 0 0 3.6.57 1 1 0 0 1 1 1V20a1 1 0 0 1-1 1A17 17 0 0 1 3 4a1 1 0 0 1 1-1h3.5a1 1 0 0 1 1 1c0 1.25.2 2.45.57 3.57a1 1 0 0 1-.25 1z"/></svg>972-55-3108642</li>
      <li><svg viewBox="0 0 24 24" aria-hidden="true"><path d="M2 5h20v14H2z M2 5l10 8 10-8" fill="none" stroke="#fff" stroke-width="2"/></svg>hello@baselinehall.net</li>
    </ul>
    <p class="back__slogan">Changing lives through tennis</p>
  </section>
</body>
</html>
```